Tallowreed Advisory Partners Business Card Design

We have the logo we just need someone to design a modern business card design.

Name: Desmond Munkalt
Phone: 3055550148
Mobile: 9175550193
Web:www.tallowreedadvisory.example
email: dmunkalt@tallowreedadvisory.example
Company: Tallowreed Advisory Partners
Title: CEO

Address: 718 Quillmore Ave, Miami, Florida 33190

Target Market(s)

companies over 100 employees

Industry/Entity Type

Business

```html
<!DOCTYPE html>
<html lang="en">
<head>
<meta charset="utf-8">
<title>Tallowreed Advisory Partners — Business Card</title>
<link rel="stylesheet" href="https://fonts.googleapis.com/css2?family=Arimo:wght@400;700&display=swap">
<style>
  :root {
    --backdrop: #8e9093;
    --card: #f7f7f5;
    --brand-blue: #3a63b5;
    --ink: #111111;
    --muted: #6f6f6f;
    --url-grey: #5a5a5a;
  }
  * { box-sizing: border-box; margin: 0; padding: 0; }
  html, body {
    width: 1200px;
    height: 1200px;
    overflow: hidden;
    background: var(--backdrop);
    font-family: "Arimo", Arial, sans-serif;
  }
  .canvas {
    position: relative;
    width: 1200px;
    height: 1200px;
    display: flex;
    flex-direction: column;
    align-items: center;
    justify-content: center;
    gap: 70px;
  }
  .card {
    position: relative;
    width: 840px;
    height: 480px;
    background: var(--card);
    box-shadow: 0 6px 18px rgba(0,0,0,0.25);
  }

  /* Front */
  .card-front {
    display: flex;
    flex-direction: column;
    align-items: center;
    justify-content: center;
    gap: 44px;
  }
  .front-brand {
    display: flex;
    align-items: center;
    gap: 32px;
  }
  .front-brand .mark {
    width: 200px;
    height: 200px;
    border-radius: 50%;
    background: var(--brand-blue);
  }
  .front-brand .brand-name {
    font-weight: 700;
    font-size: 60px;
    letter-spacing: 2px;
    color: var(--ink);
    text-transform: uppercase;
  }
  .front-url {
    font-size: 30px;
    color: var(--url-grey);
    letter-spacing: 0.5px;
  }

  /* Back */
  .card-back { padding: 40px 56px; }
  .back-brand {
    display: flex;
    align-items: center;
    gap: 26px;
  }
  .back-brand .mark {
    width: 104px;
    height: 104px;
    border-radius: 50%;
    background: var(--brand-blue);
    flex: none;
  }
  .back-brand .brand-name {
    font-weight: 700;
    color: var(--ink);
    text-transform: uppercase;
    line-height: 1;
  }
  .brand-name .line-main { display: block; font-size: 54px; letter-spacing: 2px; }
  .brand-name .line-sub { display: block; font-size: 25px; letter-spacing: 3px; margin-top: 6px; }

  .holder {
    text-align: center;
    margin-top: 34px;
  }
  .holder .name {
    font-size: 46px;
    color: var(--ink);
    text-transform: uppercase;
    letter-spacing: 1px;
  }
  .holder .title {
    font-size: 20px;
    color: var(--muted);
    margin-top: 4px;
    letter-spacing: 1px;
  }
  .contacts {
    margin-top: 34px;
    font-size: 22px;
    color: var(--ink);
    display: grid;
    grid-template-columns: 1fr 1fr;
    row-gap: 14px;
  }
  .contacts .email {
    grid-column: 1 / span 2;
    text-align: center;
  }
  .contacts .mobile { text-align: right; }
</style>
</head>
<body>
  <main class="canvas">
    <section class="card card-front" aria-label="Business card front">
      <div class="front-brand">
        <div class="mark" aria-hidden="true"></div>
        <span class="brand-name">Tallowreed</span>
      </div>
      <p class="front-url">www.tallowreedadvisory.example</p>
    </section>

    <section class="card card-back" aria-label="Business card back">
      <div class="back-brand">
        <div class="mark" aria-hidden="true"></div>
        <p class="brand-name">
          <span class="line-main">Tallowreed</span>
          <span class="line-sub">Advisory Partners</span>
        </p>
      </div>
      <div class="holder">
        <p class="name">Desmond Munkalt</p>
        <p class="title">CEO</p>
      </div>
      <div class="contacts">
        <p class="phone">Phone: 3055550148</p>
        <p class="mobile">Mobile: 9175550193</p>
        <p class="email">dmunkalt@tallowreedadvisory.example</p>
      </div>
    </section>
  </main>
</body>
</html>
```